MEDITERRANEAN Cafe Website needed

We are a MEDITERRANEAN Café serving Coffee, breakfast, Pizza, Pasta, Sandwiches etc.

We need a home page, menu & venue, Reservations & Events, Delivery
Connect (Social media / Feedback / Contact us),Join our team
Updates

Can we keep the designs in Mediterranean colours, look, and feel pleasethanks Added Saturday, December 10, 2016

Project Deadline Extended Reason: I have guarantied the payment and upgraded the project. I would like this would to give more time for new designs to come in and a couple of potential designs to show more. Added Sunday, December 11, 2016

Industry/Entity Type

Cafe

Coding

Coded - Design and coding required

Number of Pages Required

5+ page

Requirements
Must have
• MEDITERRANEAN feel, colours, style etc.
• http://www.quillandfen (DOT) co (DOT) uk
Nice to have

```html
<!DOCTYPE html>
<html lang="en">
<head>
<meta charset="utf-8">
<title>Lumea Cafe</title>
<link href="https://fonts.googleapis.com/css2?family=Playball&family=Raleway:ital,wght@0,300;0,400;0,600;0,700;1,700&display=swap" rel="stylesheet">
<style>
:root{
  --red:#f03b3b;
  --green:#3dbb3d;
  --ink:#444;
  --soft:#f4f4f4;
  --white:#fff;
}
*{box-sizing:border-box;margin:0;padding:0}
html,body{width:1200px;height:3502px;overflow:hidden}
body{font-family:"Raleway",sans-serif;color:var(--ink);background:var(--soft);position:relative}
.script{font-family:"Playball",cursive;font-weight:400}
.abs{position:absolute}
.btn{display:inline-block;border-radius:30px;font-size:13px;letter-spacing:.5px;text-align:center;text-transform:uppercase;font-weight:600}
.btn-solid{background:var(--red);color:var(--white)}
.btn-line{border:2px solid var(--red);color:var(--red);background:var(--white)}

/* header */
.site-header{left:0;top:0;width:1200px;height:86px;background:var(--white);display:flex;align-items:center;padding:0 40px}
.brand{display:flex;align-items:center;gap:10px;color:var(--green);font-weight:700;font-size:24px}
.brand-dot{width:22px;height:22px;border-radius:50%;background:var(--green)}
.main-nav{margin-left:auto;display:flex;gap:24px;font-size:13px;text-transform:uppercase;color:#333;margin-right:40px}
.main-nav .active{color:var(--red)}
.site-header .btn{width:134px;height:46px;line-height:46px}

/* hero */
.hero{left:0;top:86px;width:1200px;height:544px;background:radial-gradient(ellipse at 70% 45%,#c8583e 0%,#6e3a2c 35%,#2c2826 70%,#1d1d1d 100%)}
.hero-title{left:0;top:110px;width:1200px;text-align:center;color:var(--white);font-size:66px}
.hero-rule{left:700px;top:152px;width:190px;height:2px;background:rgba(255,255,255,.8)}
.hero-sub{left:0;top:200px;width:1200px;text-align:center;color:var(--white);font-size:32px;line-height:46px;font-weight:400}
.hero-sub em{font-weight:700}
.hero .btn{left:532px;top:310px;width:136px;height:46px;line-height:46px}
.dots{display:flex;gap:8px}
.dots span{width:11px;height:11px;border-radius:50%;border:1px solid rgba(255,255,255,.8)}
.dots span.on{background:rgba(255,255,255,.8)}
.hero .dots{left:572px;top:446px}

/* menu cards */
.card{top:584px;width:360px;height:420px;background:var(--white);text-align:center}
.card-head{height:78px;background:var(--red);color:var(--white);font-size:46px;line-height:78px}
.card-icon{margin:58px auto 0;display:block}
.card p{font-size:14px;line-height:24px;width:310px;margin:18px auto 0;color:#555}
.card .btn{width:134px;height:46px;line-height:42px;margin-top:22px}

/* location */
.location{left:0;top:1093px;width:1200px;height:548px;background:var(--white)}
.location-photo{left:0;top:0;width:586px;height:548px;background:linear-gradient(135deg,#f0d9a8 0%,#c98a4a 40%,#b53b24 75%,#6c2a1a 100%)}
.section-title{color:var(--red);font-size:48px;text-align:center}
.divider{display:flex;align-items:center;justify-content:center;gap:12px}
.divider i{display:block;width:160px;height:1px;background:#ccc}
.location .section-title{left:626px;top:80px;width:530px}
.location .divider{left:626px;top:148px;width:530px}
.location p{left:626px;top:212px;width:530px;text-align:center;font-size:15px;line-height:30px;color:#555}
.location .btn{left:821px;top:354px;width:136px;height:46px;line-height:46px}

/* gallery */
.gallery{left:0;top:1641px;width:1200px;height:888px;background:var(--soft)}
.gallery .section-title{left:0;top:42px;width:1200px}
.gallery .divider{left:0;top:110px;width:1200px}
.gallery .intro{left:320px;top:186px;width:560px;text-align:center;font-size:15px;line-height:30px;color:#555}
.tile{position:absolute;width:266px}
.tile-tall{height:460px}
.tile-half{height:220px}

/* testimonials */
.testimonials{left:0;top:2529px;width:1200px;height:542px;background:linear-gradient(90deg,#6b5440 0%,#3a3129 35%,#2e2a26 60%,#5a4a3c 100%)}
.testimonials .section-title{left:0;top:40px;width:1200px;color:var(--white)}
.testimonials .divider{left:0;top:110px;width:1200px}
.testimonials .divider i{background:rgba(255,255,255,.5)}
.quote{left:327px;top:165px;width:560px;color:var(--white);font-size:15px;line-height:31px}
.quote-name{left:327px;top:386px;color:var(--white);font-weight:700;font-size:15px}
.arrow{width:58px;height:58px;border-radius:50%;background:rgba(255,255,255,.25);display:flex;align-items:center;justify-content:center}
.testimonials .dots{left:566px;top:454px}

/* contact */
.contact{left:0;top:3071px;width:1200px;height:369px;background:var(--soft)}
.info-col{top:70px;width:360px;text-align:center;font-size:14px;line-height:24px;color:#444}
.info-col h3{font-size:21px;font-weight:400;letter-spacing:.5px;margin:16px 0 22px;color:#333}
.info-col strong{font-weight:700}
.socials{display:flex;gap:12px;justify-content:center}
.socials span{width:34px;height:34px;border-radius:50%;border:2px solid var(--red)}

.site-footer{left:0;top:3440px;width:1200px;height:62px;background:var(--red);color:var(--white);font-size:12px;text-align:center;line-height:62px;letter-spacing:.5px}
</style>
</head>
<body>

<header class="site-header abs">
  <div class="brand"><span class="brand-dot"></span>Lumea</div>
  <nav class="main-nav">
    <span class="active">Homepage</span><span>Menu</span><span>Location</span><span>Events</span><span>Delivery</span><span>Join Team</span>
  </nav>
  <span class="btn btn-solid">Book a Table</span>
</header>

<section class="hero abs" role="img" aria-label="Salmon fillet with olive oil, tomatoes, basil and peppercorns on a dark board">
  <h1 class="hero-title abs script">Welcome</h1>
  <div class="hero-rule abs"></div>
  <p class="hero-sub abs">Awesome <em>Mediterranean</em><br>Experience Starts Here</p>
  <span class="btn btn-solid abs">View Menu</span>
  <div class="dots abs"><span></span><span></span><span class="on"></span></div>
</section>

<article class="card abs" style="left:40px">
  <div class="card-head script">Food</div>
  <svg class="card-icon" width="96" height="66" viewBox="0 0 96 66" fill="none" stroke="#3dbb3d" stroke-width="4" stroke-linejoin="round">
    <path d="M8 26 C8 6 88 6 88 26 Z"/><path d="M4 36 Q16 30 28 36 T52 36 T76 36 T94 36"/><rect x="6" y="42" width="84" height="8" rx="3"/><path d="M10 54 H86 Q86 62 78 62 H18 Q10 62 10 54 Z"/>
  </svg>
  <p>Give your taste buds a treat and experience authentic Mediterranean food at Lumea . Make Lumea cafe your next casual dinning destination</p>
  <span class="btn btn-line">View Menu</span>
</article>

<article class="card abs" style="left:420px">
  <div class="card-head script">Desserts</div>
  <svg class="card-icon" width="80" height="110" viewBox="0 0 80 110" fill="none" stroke="#3dbb3d" stroke-width="4" stroke-linejoin="round" style="margin-top:36px">
    <circle cx="46" cy="12" r="7"/><path d="M12 50 Q10 30 30 28 Q40 18 56 26 Q72 30 68 50 Z"/><path d="M6 50 H74 L66 106 H14 Z"/><path d="M26 58 L30 104 M40 58 V104 M54 58 L50 104"/>
  </svg>
  <p style="margin-top:10px">Give your taste buds a treat and experience authentic Mediterranean food at Lumea . Make Lumea cafe your next casual dinning destination</p>
  <span class="btn btn-line">View Menu</span>
</article>

<article class="card abs" style="left:800px">
  <div class="card-head script">Drinks</div>
  <svg class="card-icon" width="100" height="110" viewBox="0 0 100 110" fill="none" stroke="#3dbb3d" stroke-width="4" stroke-linejoin="round" style="margin-top:36px">
    <circle cx="24" cy="22" r="14"/><path d="M10 36 H90 L50 72 Z"/><path d="M50 72 V102 M32 104 H68"/><path d="M56 46 L80 8"/>
  </svg>
  <p style="margin-top:10px">Give your taste buds a treat and experience authentic Mediterranean food at Lumea . Make Lumea cafe your next casual dinning destination</p>
  <span class="btn btn-line">View Menu</span>
</article>

<section class="location abs">
  <div class="location-photo abs" role="img" aria-label="Cafe interior with patterned arched windows, lanterns and a long red sofa with cushions"></div>
  <h2 class="section-title abs script">Location</h2>
  <div class="divider abs"><i></i><svg width="16" height="16" viewBox="0 0 16 16" fill="none" stroke="#3dbb3d" stroke-width="1.5"><path d="M8 2 L14 8 L8 14 L2 8 Z"/></svg><i></i></div>
  <p class="abs">Located in Coral Bay, Lumea Cafe has become a beacon for Service and Quality food.Enjoy an after-dinner coffee or drink from the spacious waterfront magical outdoors of the Marina or our comfortable indoor where you can relax and spend a memorable time with us.</p>
  <span class="btn btn-solid abs">Book a Table</span>
</section>

<section class="gallery abs">
  <h2 class="section-title abs script">Gallery</h2>
  <div class="divider abs"><i></i><svg width="16" height="16" viewBox="0 0 16 16" fill="none" stroke="#3dbb3d" stroke-width="1.5"><path d="M8 2 L14 8 L8 14 L2 8 Z"/></svg><i></i></div>
  <p class="intro abs">Located in Coral Bay, Lumea Cafe has become a beacon for Service and Quality food.Enjoy an after-dinner</p>
  <div class="tile tile-tall" style="left:40px;top:292px;background:linear-gradient(180deg,#dfe6ea 0%,#9fb0a8 45%,#4d6a7a 75%,#2b3a30 100%)" role="img" aria-label="Glass of white wine by the marina"></div>
  <div class="tile tile-half" style="left:325px;top:292px;background:radial-gradient(circle,#d9c58a 0%,#b89a52 60%,#6e5a3a 100%)" role="img" aria-label="Pizza with olives and onion"></div>
  <div class="tile tile-half" style="left:325px;top:532px;background:radial-gradient(circle,#e8c070 0%,#efe6d2 55%,#dcd2c0 100%)" role="img" aria-label="Bowl of hummus with paprika"></div>
  <div class="tile tile-tall" style="left:610px;top:292px;background:linear-gradient(180deg,#d2a07a 0%,#e08a8a 40%,#d76f78 70%,#9b6a48 100%)" role="img" aria-label="Pink smoothie with a straw on a wooden table"></div>
  <div class="tile tile-half" style="left:895px;top:292px;background:radial-gradient(circle,#e8c070 0%,#efe6d2 55%,#dcd2c0 100%)" role="img" aria-label="Bowl of hummus with paprika"></div>
  <div class="tile tile-half" style="left:895px;top:532px;background:linear-gradient(135deg,#efe2c4 0%,#b99866 45%,#a33c2a 80%,#5c2a1c 100%)" role="img" aria-label="Cafe interior with arched windows and red seating"></div>
</section>

<section class="testimonials abs" role="img" aria-label="Two guests laughing together at a cafe table">
  <h2 class="section-title abs script">Testimonials</h2>
  <div class="divider abs"><i></i><svg width="16" height="16" viewBox="0 0 16 16" fill="none" stroke="#ffffff" stroke-width="1.5"><path d="M8 2 L14 8 L8 14 L2 8 Z"/></svg><i></i></div>
  <p class="quote abs">We have visited the restaurant once a fort night since it opened, and have found that the menu changes often. The standard of the food has dropped since the first time I ate here and they have added a wider variety of foods outside their Mediterranean theme. Fantastic location and ambience, however little focus on the quality and consistency of...</p>
  <p class="quote-name abs">Elena R</p>
  <div class="arrow abs" style="left:134px;top:2300px;top:256px"><svg width="14" height="20" viewBox="0 0 14 20" fill="none" stroke="#fff" stroke-width="3"><path d="M11 2 L3 10 L11 18"/></svg></div>
  <div class="arrow abs" style="left:1005px;top:256px"><svg width="14" height="20" viewBox="0 0 14 20" fill="none" stroke="#fff" stroke-width="3"><path d="M3 2 L11 10 L3 18"/></svg></div>
  <div class="dots abs"><span class="on"></span><span></span><span></span></div>
</section>

<section class="contact abs">
  <div class="info-col abs" style="left:0">
    <svg width="24" height="32" viewBox="0 0 24 32" fill="#f03b3b"><path d="M12 0 C5 0 0 5 0 12 C0 21 12 32 12 32 C12 32 24 21 24 12 C24 5 19 0 12 0 Z M12 16 A4 4 0 1 1 12 8 A4 4 0 1 1 12 16 Z"/></svg>
    <h3>CONTACT</h3>
    <p>12 Harbour Walk | Coral Bay, Singapore<br>091234, Singapore<br>6200 0147<br>info@lumeacafe.com<br>or reservations@lumeacafe.com</p>
  </div>
  <div class="info-col abs" style="left:420px">
    <svg width="30" height="30" viewBox="0 0 30 30" fill="none" stroke="#f03b3b" stroke-width="3"><circle cx="15" cy="15" r="12"/><path d="M15 8 V15 L20 18"/></svg>
    <h3>OPENING HOURS</h3>
    <p><strong>Monday- Thursday - Friday</strong><br>8:30 - 3pm and 5:30pm till 10pm<br><strong>Tuesday- Saturday - Sunday</strong><br>and public holiday 8am till 10pm<br><strong>Wednesday</strong> -Close</p>
  </div>
  <div class="info-col abs" style="left:796px">
    <svg width="28" height="30" viewBox="0 0 28 30" fill="#f03b3b"><circle cx="22" cy="5" r="5"/><circle cx="6" cy="15" r="5"/><circle cx="22" cy="25" r="5"/><path d="M22 5 L6 15 L22 25" stroke="#f03b3b" stroke-width="2.5" fill="none"/></svg>
    <h3>SOCIAL SHARE</h3>
    <div class="socials" aria-label="Social links"><span></span><span></span><span></span><span></span></div>
  </div>
</section>

<footer class="site-footer abs">LUMEA CAFE © 2015. ALL RIGHTS RESERVED.</footer>

</body>
</html>
```